Business Card Design

We currently have a business card design for our main business 'Lantern Walls"
We are reasonably happy with our current design for Lantern Walls business card (black damask patterned wallpaper in background white simplistic font with white chandelier (see logo on website). www.lanternwalls.com.au

We are considering whether its in our best interest to have a separate business card OR a double sided card to promote our secondary business 'Glow Cones'. We are open to either a double-sided card with one business on each side OR a double sided card for each business. With contact info on the back of each.

We need a new snazzy design for 'Glow Cones' our custom made lampshades from which we craft from our wallpaper designs. We had an idea that we could use the top swatch shown on this link below as the pattern in the background (Orange/black) geometric triangles.
http://www.lanternwalls.com.au/product_info.php?products_id=1086

For the glow cones Font we would be happy with something similar to Lantern Walls but perhaps a little more handmade/arty slant.
Below another link shows you a few of our lampshades
http://www.lanternwalls.com.au/index.php?cPath=10

For Glow Cones I think we also need the quote under in smaller font
"Custom-Made Wallpaper Lampshades"

Target Market(s)

Glow Cones will be for the Young Funky Apartment Dwellers, Young Families Styling Home Decor and Kids Rooms. It also attracts small business owners doing shop-fits.

Industry/Entity Type

Business

Contact Information for Business Card

We need to incorporate our sister business to the back side of our business card. I am also open to having two different business cards if designers think this will not be possible.
We need the same contact info, different logo.
ABN: 47 302 916 584
Email: sales@lanternwalls.com.au
Postal Address: PO Box 731, Kelvale VIC 3294
Website: http://www.lanternwalls.com.au

Requirements
Must have
• A hand-made arty appeal for Glow Cones
Was unable to get sliders to work for the look and feel so below is the best list from the above:
Bold, Playful, Modern, Personable, Colorful, Upmarket.
Nice to have
• We love the bold contrasting colors. Colors chosen for our website were Orange, Blue and Duck Egg Bright Blue!

```html
<!DOCTYPE html>
<html lang="en">
<head>
<meta charset="utf-8">
<title>Glow Cones – Business Card</title>
<link rel="stylesheet" href="https://fonts.googleapis.com/css2?family=Arimo:wght@400;700&display=swap">
<style>
  :root {
    --card-bg: #ffffff;
    --brand-grey: #c4c4c4;
    --abn-orange: #f07f2a;
    --email-teal: #3a8fa0;
    --web-pink: #e5267d;
    --address-grey: #7a7a7a;
    --art-pink: #e94b93;
    --art-dark: #3a3436;
    --art-lime: #c9d43a;
    --art-cream: #ecebe2;
  }
  html, body {
    margin: 0;
    padding: 0;
    overflow: hidden;
    background: var(--card-bg);
  }
  .card {
    position: relative;
    width: 1200px;
    height: 741px;
    background: var(--card-bg);
    overflow: hidden;
    font-family: "Arimo", Arial, sans-serif;
  }
  .lamp-art {
    position: absolute;
    left: 145px;
    top: 120px;
    width: 356px;
    height: 540px;
  }
  .brand-name {
    position: absolute;
    left: 549px;
    top: 402px;
    margin: 0;
    font-size: 80px;
    font-weight: 700;
    letter-spacing: 1px;
    line-height: 1;
    color: var(--brand-grey);
    white-space: nowrap;
  }
  .contact {
    position: absolute;
    left: 548px;
    top: 526px;
    margin: 0;
    padding: 0;
    list-style: none;
    font-size: 26px;
    line-height: 32px;
    white-space: nowrap;
  }
  .contact .abn { color: var(--abn-orange); }
  .contact .email { color: var(--email-teal); }
  .contact .website { color: var(--web-pink); }
  .contact .address { color: var(--address-grey); }
</style>
</head>
<body>
  <main class="card">
    <svg class="lamp-art" viewBox="0 0 356 540" role="img" aria-label="Table lamp illustration covered in a pink, black, lime and orange geometric triangle wallpaper pattern">
      <defs>
        <linearGradient id="lampTones" x1="0" y1="0" x2="1" y2="1">
          <stop offset="0" stop-color="var(--art-dark)"/>
          <stop offset="0.35" stop-color="var(--art-pink)"/>
          <stop offset="0.65" stop-color="var(--art-cream)"/>
          <stop offset="1" stop-color="var(--art-lime)"/>
        </linearGradient>
      </defs>
      <rect x="0" y="0" width="356" height="540" rx="6" fill="url(#lampTones)" opacity="0.85"/>
    </svg>

    <h1 class="brand-name">Glow Cones</h1>

    <ul class="contact">
      <li class="abn">ABN: 47 302 916 584</li>
      <li class="email">Email: sales@lanternwalls.com.au</li>
      <li class="website">Website: http://www.lanternwalls.com.au</li>
      <li class="address">Postal Address: PO Box 731, Kelvale VIC 3294</li>
    </ul>
  </main>
</body>
</html>
```